E-Waste Recycling Company Business Card

New Electronic Recycling Company based in Long Island, New York called "Baron Rustwell" We take outdated computers, components, electrical wire, circuit breakers, ink cartridges, etc. We look mostly for donated items that we recycle for our customers but will pay for large quantities from businesses. The design should reflect that we are environmentally friendly and our unique Quadra Purge process that ensures all personal data is wiped clean off hard drives. Please use our attached logo
Electrical

```html
<!DOCTYPE html>
<html lang="en">
<head>
<meta charset="utf-8">
<title>Baron Rustwell – Business Card</title>
<link href="https://fonts.googleapis.com/css2?family=Open+Sans:wght@400;600;700&display=swap" rel="stylesheet">
<style>
  :root {
    --page: #ffffff;
    --green-light: #86bd52;
    --green-mid: #7cb64a;
    --green-deep: #8cbf4f;
    --ink: #ffffff;
    --tag-bg: #1f1a21;
    --divider: rgba(255, 255, 255, 0.75);
  }
  * { box-sizing: border-box; margin: 0; padding: 0; }
  html, body {
    width: 1200px;
    height: 1000px;
    overflow: hidden;
    background: var(--page);
    font-family: "Open Sans", Arial, sans-serif;
    color: var(--ink);
  }
  .canvas { position: relative; width: 1200px; height: 1000px; }
  .card {
    position: absolute;
    left: 194px;
    width: 812px;
    height: 488px;
    background:
      radial-gradient(ellipse at 45% 45%, var(--green-light) 0%, transparent 60%),
      linear-gradient(100deg, var(--green-mid) 0%, var(--green-deep) 100%);
    overflow: hidden;
  }
  .card--front { top: 4px; }
  .card--back { top: 506px; }

  .brand-name {
    position: absolute;
    font-weight: 600;
    color: var(--ink);
    white-space: nowrap;
    transform: translate(-50%, -50%);
  }
  .card--front .brand-name { left: 406px; top: 240px; font-size: 46px; }
  .card--back .brand-name { left: 216px; top: 246px; font-size: 34px; }

  .divider {
    position: absolute;
    left: 410px;
    top: 58px;
    width: 2px;
    height: 374px;
    background: linear-gradient(to bottom, transparent, var(--divider) 20%, var(--divider) 80%, transparent);
  }

  .details { position: absolute; left: 450px; top: 114px; }
  .service {
    font-size: 23px;
    font-weight: 700;
    letter-spacing: 0.5px;
    line-height: 1;
    margin-bottom: 14px;
  }
  .tag {
    display: inline-block;
    background: var(--tag-bg);
    font-size: 16px;
    font-weight: 700;
    letter-spacing: 0.8px;
    line-height: 22px;
    padding: 0 7px;
    margin-bottom: 8px;
  }
  .tags { display: flex; flex-direction: column; align-items: flex-start; }
  .contact { font-size: 18px; line-height: 26px; margin-top: 10px; }
  .contact li { list-style: none; margin-bottom: 18px; }
</style>
</head>
<body>
<div class="canvas">
  <section class="card card--front">
    <div class="brand-name">Baron Rustwell</div>
  </section>

  <section class="card card--back">
    <div class="brand-name">Baron Rustwell</div>
    <div class="divider"></div>
    <div class="details">
      <h2 class="service">ELECTRONIC RECYCLING</h2>
      <div class="tags">
        <span class="tag">ENVIRONMENTALLY FRIENDLY</span>
        <span class="tag">UNIQUE QUADRA PURGE</span>
      </div>
      <ul class="contact">
        <li>www.baronrustwell.com</li>
        <li>+3 8050 71-28-406</li>
        <li>5678 Birch st., Cityname,<br>LA, 10101</li>
      </ul>
    </div>
  </section>
</div>
</body>
</html>
```